Best in class business looking for best in class stationery that accurately reflects the brand image we are trying to build as the brand expands throughout the country. The Varying items should be an eye catching design that makes even the simplest letter or small business card stand out in the crowd.

Target Market(s)

Professionals

Industry/Entity Type

Real Estate

Other font styles liked:
• See atttached logo

Requirements
Must have
• Letterhead
• Business cards
• Envelopes
• Labels for larger mailings
Nice to have
• Folders
• Notebook
Should not have
• Stale design elements

```html
<!DOCTYPE html>
<html lang="en">
<head>
<meta charset="utf-8">
<title>Crestline Management Corporation — Stationery</title>
<link href="https://fonts.googleapis.com/css2?family=Lato:wght@300;400;700&display=swap" rel="stylesheet">
<style>
  :root {
    --navy: #1f1f5c;
    --royal: #233c95;
    --royal-soft: rgba(35, 60, 149, 0.08);
    --paper: #f3f3f5;
    --backdrop: #e6e6ea;
    --ink: #2a2a3a;
    --rule: #c9c9d2;
    --lavender: #a4a8dc;
    --faint: #c4c8de;
  }
  * { box-sizing: border-box; margin: 0; padding: 0; }
  html, body { width: 1200px; height: 800px; overflow: hidden; }
  body {
    background: var(--backdrop);
    font-family: "Lato", sans-serif;
    color: var(--ink);
    position: relative;
  }
  .piece {
    position: absolute;
    background: var(--paper);
    overflow: hidden;
    box-shadow: 0 2px 6px rgba(0,0,0,0.12);
  }
  .edge-band { position: absolute; left: 0; top: 0; bottom: 0; background: var(--navy); }

  /* company name lockup: one font, one weight, one colour */
  .brand {
    position: absolute;
    display: flex; align-items: center; gap: 0.6em;
    color: var(--navy); font-weight: 400; letter-spacing: 0.06em;
    text-align: center; line-height: 1.25; white-space: nowrap;
  }
  .brand-square { width: 1.3em; height: 1.3em; background: var(--navy); flex: none; }

  /* corner decoration area */
  .corner-art {
    position: absolute; right: 0; bottom: 0;
    background:
      linear-gradient(90deg, transparent 0 12%, var(--royal-soft) 12% 100%),
      linear-gradient(to top left, var(--royal) 0%, var(--navy) 38%, rgba(35,60,149,0.55) 70%, rgba(35,60,149,0.06) 100%);
  }

  /* envelope front */
  .envelope-front { left: 52px; top: 260px; width: 428px; height: 204px; }
  .envelope-front .edge-band { width: 13px; }
  .envelope-front .brand { left: 44px; top: 44px; font-size: 9px; }
  .envelope-front .corner-art { width: 202px; height: 130px; }

  /* envelope back */
  .envelope-back { left: 32px; top: 502px; width: 448px; height: 218px; background: var(--navy); }
  .envelope-flap {
    position: absolute; left: 20px; right: 12px; top: 0; height: 102px;
    background: var(--lavender); border-radius: 0 0 14px 14px;
  }
  .envelope-flap::before {
    content: ""; position: absolute; left: 0; right: 0; top: 0; height: 54px;
    background: var(--navy); border-radius: 0 0 12px 12px;
  }
  .envelope-flap::after {
    content: ""; position: absolute; left: 0; right: 0; bottom: 0; height: 30px;
    background: var(--paper); border-radius: 0 0 14px 14px;
  }
  .emboss-square {
    position: absolute; left: 40px; bottom: 24px; width: 46px; height: 46px;
    background: #26266a; box-shadow: 1px 1px 0 #15153f, -1px -1px 0 #30307a;
  }

  /* letterhead */
  .letterhead { left: 524px; top: 160px; width: 412px; height: 562px; }
  .letterhead .edge-band { width: 20px; }
  .letterhead .brand { left: 50%; transform: translateX(-50%); top: 60px; font-size: 12px; }
  .letter-body { position: absolute; left: 34px; top: 144px; width: 330px; font-size: 6.9px; line-height: 10.3px; font-weight: 400; color: #3a3a44; }
  .letter-body p { margin-bottom: 10px; text-align: justify; }
  .letter-body .salutation { margin-bottom: 12px; }
  .letter-footer { position: absolute; left: 34px; bottom: 42px; width: 170px; font-size: 4.6px; line-height: 6.4px; font-weight: 700; }
  .letterhead .corner-art { width: 216px; height: 136px; }

  /* business cards */
  .card-front { left: 944px; top: 164px; width: 176px; height: 92px; }
  .card-front .brand { left: 50%; top: 36px; transform: translateX(-50%); font-size: 6.6px; }

  .card-back { left: 952px; top: 294px; width: 180px; height: 98px; }
  .card-back .edge-band { width: 10px; }
  .card-name { position: absolute; left: 24px; top: 20px; font-size: 9.5px; line-height: 11px; font-weight: 300; }
  .card-title { position: absolute; left: 24px; top: 46px; font-size: 3.8px; font-weight: 700; letter-spacing: 0.03em; }
  .card-contact { position: absolute; left: 24px; top: 58px; font-size: 3.8px; line-height: 5px; }
  .card-back .corner-art { width: 94px; height: 70px; }

  /* notepad */
  .notepad { left: 960px; top: 528px; width: 208px; height: 192px; }
  .notepad .brand { left: 50%; top: 14px; transform: translateX(-50%); font-size: 5.2px; }
  .note-lines { position: absolute; left: 22px; right: 30px; top: 45px; }
  .note-lines span { display: block; height: 10.3px; border-bottom: 0.6px solid var(--rule); }
  .notepad .faint-art {
    position: absolute; right: 2px; bottom: 14px; width: 124px; height: 82px;
    background: linear-gradient(to top left, var(--faint), rgba(196,200,222,0.15));
  }
  .note-footer { position: absolute; left: 36px; right: 22px; bottom: 14px; font-size: 3px; line-height: 4px; text-align: center; }
</style>
</head>
<body>

  <section class="piece envelope-front" aria-label="Envelope front">
    <div class="edge-band"></div>
    <div class="brand"><span class="brand-square"></span><span>CRESTLINE MANAGEMENT<br>CORPORATION</span></div>
    <div class="corner-art" role="img" aria-label="Large brand decoration in navy and royal blue"></div>
  </section>

  <section class="piece envelope-back" aria-label="Envelope back">
    <div class="envelope-flap"></div>
    <div class="emboss-square"></div>
  </section>

  <section class="piece letterhead" aria-label="Letterhead">
    <div class="edge-band"></div>
    <div class="brand"><span class="brand-square"></span><span>CRESTLINE MANAGEMENT<br>CORPORATION</span></div>
    <div class="letter-body">
      <p class="salutation">Lorem ipsum</p>
      <p>Dolor sit amet, consectetur adipiscing elit. Curabitur ultrices congue orci ac malesuada. Nam posuere arcu magna, at placerat nisl tempus nec. Phasellus suscipit sapien quis tempus convallis. Vestibulum aliquam eros nec diam viverra, tempor euismod nunc dapibus. Donec ultricies metus a ipsum viverra vestibulum. Duis vel aliquet velit. Quisque commodo odio eu turpis rhoncus tincidunt. Aliquam sit amet neque arcu. Aenean sed arcu nec ligula posuere venenatis. Pellentesque vitae magna elementum, tincidunt dolor et, porttitor ligula. Quisque vestibulum dapibus tellus. Aliquam leo ante, scelerisque sit amet lacinia sed, laoreet ac tortor. Cras id commodo dolor. Sed placerat interdum vehicula. Maecenas imperdiet rhoncus dui ut varius.</p>
      <p>Duis mollis varius sagittis. Vestibulum ante ipsum primis in faucibus orci luctus et ultrices posuere cubilia Curae; Maecenas ullamcorper varius diam, ac malesuada est. Sed accumsan odio et mi laoreet, in aliquam ante tempor. Praesent ut rhoncus nibh. Ut vel sodales enim, ac tempor nisl. Suspendisse convallis malesuada leo, et hendrerit risus lobortis vitae. Suspendisse consectetur purus sed mauris vehicula, pellentesque vehicula risus blandit. Quisque ut velit vulputate, placerat elit id, tincidunt lectus. Aenean vel justo iaculis, rutrum metus non, faucibus mi. Maecenas mauris dolor, posuere venenatis auctor eu, fermentum vitae libero. Mauris sit amet condimentum tellus. Ut et dapibus ante, eu tincidunt lorem. Curabitur iaculis eros et libero posuere varius. Vivamus vel lacus erat.</p>
      <p>Aliquam in ante nec sapien commodo varius. Vivamus sit amet venenatis augue. Aliquam vitae orci nulla. Proin non molestie lacus. Fusce eu pulvinar dolor. Nullam metus enim, pulvinar sed velit nec, pulvinar viverra metus. Pellentesque lacinia, arcu condimentum pulvinar rutrum, massa tortor porttitor tortor, eu elementum eros nisi id neque. Phasellus accumsan ligula fermentum, dignissim arcu non, tristique mauris. Curabitur scelerisque metus tortor, at dapibus urna gravida quis. Vivamus sed dolor elit. Nulla fermentum laoreet urna, sed aliquam risus lobortis nec. Aliquam sed cursus nunc, et sollicitudin nunc.</p>
    </div>
    <p class="letter-footer">Lorem ipsum dolor sit amet, consectetur adipiscing elit. Curabitur ultrices tempus nec. Phasellus suscipit sapien quis tempus convallis. Vestibulum</p>
    <div class="corner-art" role="img" aria-label="Large brand decoration in navy and royal blue"></div>
  </section>

  <section class="piece card-front" aria-label="Business card front">
    <div class="brand"><span class="brand-square"></span><span>CRESTLINE MANAGEMENT<br>CORPORATION</span></div>
  </section>

  <section class="piece card-back" aria-label="Business card back">
    <div class="edge-band"></div>
    <p class="card-name">Marta<br>Nowicka</p>
    <p class="card-title">STARSZA BRYGADZISTKA</p>
    <p class="card-contact">m.nowicka@crestline.pl<br>210 555 014</p>
    <div class="corner-art" role="img" aria-label="Brand decoration in navy and royal blue"></div>
  </section>

  <section class="piece notepad" aria-label="Notepad">
    <div class="brand"><span class="brand-square"></span><span>CRESTLINE MANAGEMENT<br>CORPORATION</span></div>
    <div class="note-lines">
      <span></span><span></span><span></span><span></span><span></span><span></span>
      <span></span><span></span><span></span><span></span><span></span>
    </div>
    <div class="faint-art" role="img" aria-label="Faint brand decoration in pale blue"></div>
    <p class="note-footer">Lorem ipsum dolor sit amet, consectetur adipiscing elit. Nam posuere arcu magna, at placerat.</p>
  </section>

</body>
</html>
```